Innovative Healthcare Technology Company needs a Business Card Design

We are in need of an innovative business card design for a new healthcare software company called "Lumenwise Data Partners". We develop software that creates medical assessment applications and mobile e-learning prevention services to reduce risk behaviors in adolescent and young adults. Our initial product, the "KESTREL App", conducts a tailored sexual risk assessment and provides a doctor with an insightful patient report to improve sexual risk counseling and ultimately reduce unintended pregnancy, STDs, etc.

We would like the design to incorporate our logo and branding colors (attached) in an innovative and creative manner. The final design should communicate professionalism and healthcare innovation. Our tag line is "prevention is the solution" (doesn't necessarily need to be included) and our target audience is doctors, medical directors, and medical business administrators. Please visit our website for additional info ourbrightmarq.com. Be creative and we look forward to seeing your designs!

Target Market(s)

healthcare - doctors, medical directors and medical business administrators

Industry/Entity Type

Healthcare

Contact Information for Business Card

We would like the design to incorporate our logo and branding colors (attached) in an innovative and creative manner. The final design should communicate professionalism and healthcare innovation. Our tag line is "prevention is the solution" (doesn't necessarily need to be included)

Font styles to use
Other font styles liked:
• quicksand

Requirements
Must have
• our logo and brand colors
• Name, (Mara Feldhovenik, PhD)
• Email (drmara@ourbrightmarq.com)
• phone (555.283.9170)
• Website (ourbrightmarq.com)
Should not have
• cartoon look

```html
<!DOCTYPE html>
<html lang="en">
<head>
<meta charset="utf-8">
<title>Lumenwise Data Partners — Business Card</title>
<link href="https://fonts.googleapis.com/css2?family=Quicksand:wght@400;500&display=swap" rel="stylesheet">
<style>
  :root {
    --backdrop: #696968;
    --card: #f6f6f4;
    --brand-blue: #1f5a9a;
    --brand-green: #5b8a73;
    --text-grey: #7a7a7a;
    --icon-blue: #24589a;
  }
  * { margin: 0; padding: 0; box-sizing: border-box; }
  html, body {
    width: 1200px; height: 1200px; overflow: hidden;
    background: var(--backdrop);
    font-family: "Quicksand", sans-serif;
  }
  .canvas { position: relative; width: 1200px; height: 1200px; }
  .card {
    position: absolute; left: 220px;
    width: 760px; height: 434px;
    background: var(--card);
    box-shadow: 0 6px 18px rgba(0,0,0,0.25);
  }
  .card--contact { top: 130px; }
  .card--brand { top: 636px; }

  .brand-lockup { position: absolute; display: flex; align-items: center; }
  .brand-lockup__mark { background: var(--brand-blue); flex: none; }
  .brand-lockup__name {
    color: var(--brand-blue); font-weight: 500; line-height: 1.05;
  }

  .card--contact .brand-lockup { left: 60px; top: 236px; gap: 14px; }
  .card--contact .brand-lockup__mark { width: 30px; height: 30px; }
  .card--contact .brand-lockup__name { font-size: 25px; }

  .card--brand .brand-lockup { left: 150px; top: 160px; gap: 26px; }
  .card--brand .brand-lockup__mark { width: 64px; height: 64px; }
  .card--brand .brand-lockup__name { font-size: 50px; }

  .contact { position: absolute; left: 400px; top: 70px; color: var(--text-grey); }
  .contact__name { font-size: 31px; font-weight: 400; letter-spacing: 1px; margin-bottom: 18px; }
  .contact__name .credential { font-size: 18px; }
  .contact__list { list-style: none; }
  .contact__item {
    display: flex; align-items: center; gap: 14px;
    font-size: 20px; height: 38px;
  }
  .contact__icon { width: 22px; height: 22px; flex: none; }
</style>
</head>
<body>
<div class="canvas">

  <section class="card card--contact">
    <div class="brand-lockup">
      <span class="brand-lockup__mark"></span>
      <span class="brand-lockup__name">Lumenwise<br>Data Partners</span>
    </div>

    <div class="contact">
      <p class="contact__name">Mara Feldhovenik, <span class="credential">PhD</span></p>
      <ul class="contact__list">
        <li class="contact__item">
          <svg class="contact__icon" viewBox="0 0 24 24" aria-hidden="true">
            <rect x="2" y="5" width="20" height="14" fill="var(--icon-blue)"/>
            <path d="M2 5 L12 13 L22 5" fill="none" stroke="#f6f6f4" stroke-width="1.6"/>
          </svg>
          drmara@ourbrightmarq.com
        </li>
        <li class="contact__item">
          <svg class="contact__icon" viewBox="0 0 24 24" aria-hidden="true">
            <path d="M3 9 Q12 2 21 9 L19 11 L16 10 L16 8 Q12 6.5 8 8 L8 10 L5 11 Z" fill="var(--icon-blue)"/>
            <rect x="5" y="12" width="14" height="9" rx="1" fill="var(--icon-blue)"/>
            <circle cx="12" cy="16.5" r="2.2" fill="#f6f6f4"/>
          </svg>
          555.283.9170
        </li>
        <li class="contact__item">
          <svg class="contact__icon" viewBox="0 0 24 24" aria-hidden="true">
            <g fill="none" stroke="var(--icon-blue)" stroke-width="1.6">
              <circle cx="12" cy="12" r="9"/>
              <ellipse cx="12" cy="12" rx="4" ry="9"/>
              <line x1="3" y1="12" x2="21" y2="12"/>
            </g>
          </svg>
          ourbrightmarq.com
        </li>
      </ul>
    </div>
  </section>

  <section class="card card--brand">
    <div class="brand-lockup">
      <span class="brand-lockup__mark"></span>
      <span class="brand-lockup__name">Lumenwise<br>Data Partners</span>
    </div>
  </section>

</div>
</body>
</html>
```